Business Card Design

I give lessons and clinics for dressage riders
I would like the design to be an outline (with broad lines) of a dressage horse and rider with in background of whole card with print over top tan or parchment card with burgundy print

Industry/Entity Type

Business

Contact Information for Business Card

Ned Carrow
617-354-2790
Classical dressage training for the modern American
Clinics, lessons, training level -Prix St. George

Requirements
Must have
• broad lined outline of dressage horse and rider

```html
<!DOCTYPE html>
<html lang="en">
<head>
<meta charset="utf-8">
<title>Ned Carrow — Dressage Training Card</title>
<link rel="stylesheet" href="https://fonts.googleapis.com/css2?family=Alegreya+SC:wght@400;500&family=Alegreya:ital,wght@1,400&display=swap">
<style>
  :root {
    --parchment: #f3dfae;
    --parchment-light: #f7e7c0;
    --parchment-warm: #e9b86e;
    --burgundy: #891b41;
    --cream: #f6e3b3;
  }
  html, body {
    margin: 0;
    padding: 0;
    width: 702px;
    height: 1200px;
    overflow: hidden;
    background: var(--parchment);
  }
  .card {
    position: relative;
    width: 702px;
    height: 1200px;
    overflow: hidden;
    background:
      radial-gradient(ellipse at 0% 25%, rgba(233,184,110,0.55), rgba(233,184,110,0) 45%),
      radial-gradient(ellipse at 70% 30%, var(--parchment-light), var(--parchment) 70%);
  }
  .card__art {
    position: absolute;
    inset: 0;
    width: 702px;
    height: 1200px;
  }
  .card__text {
    position: absolute;
    left: 75px;
    margin: 0;
    color: var(--cream);
    line-height: 1;
    white-space: nowrap;
  }
  .card__name {
    top: 612px;
    font-family: "Alegreya SC", Georgia, serif;
    font-weight: 400;
    font-size: 74px;
    letter-spacing: 3px;
  }
  .card__phone {
    top: 728px;
    font-family: "Alegreya SC", Georgia, serif;
    font-weight: 400;
    font-size: 54px;
    letter-spacing: 8px;
  }
  .card__tagline {
    top: 806px;
    font-family: "Alegreya", Georgia, serif;
    font-style: italic;
    font-size: 39px;
    line-height: 66px;
    letter-spacing: 0.5px;
  }
  .card__tagline span { display: block; }
</style>
</head>
<body>
  <main class="card">
    <svg class="card__art" viewBox="0 0 702 1200" xmlns="http://www.w3.org/2000/svg">
      <defs>
        <radialGradient id="rider-tone" cx="45%" cy="45%" r="60%">
          <stop offset="0" stop-color="#891b41" stop-opacity="0.22"/>
          <stop offset="1" stop-color="#891b41" stop-opacity="0"/>
        </radialGradient>
      </defs>
      <rect class="card__illustration" role="img"
            aria-label="Broad-line burgundy outline of a dressage horse and rider jumping, its back flowing into the band below"
            x="60" y="25" width="590" height="400" rx="40" fill="url(#rider-tone)"/>
      <path class="card__band"
            d="M0,603 C130,500 340,455 600,440 C628,412 622,345 642,335 C668,372 690,430 702,500 L702,1200 L0,1200 Z"
            fill="var(--burgundy)"/>
    </svg>

    <h1 class="card__text card__name">Ned Carrow</h1>
    <p class="card__text card__phone">617–354–2790</p>
    <p class="card__text card__tagline">
      <span>Classical dressage training</span>
      <span>for the modern American Clinics,</span>
      <span>lessons, training level –</span>
      <span>Prix St. George</span>
    </p>
  </main>
</body>
</html>
```